Varlo Building Pty Ltd need an Identity!

We need a logo design for a building company based in Sydney, Australia. In addition - Business Card Layout. The colour scheme is to be black and red and communicate a professional yet 'hands on' approach to building.

Target Market(s)

Architects, Home Owners, Developers

Industry/Entity Type

Construction

Font styles to use
Serif
Sans Serif

Colors
ec1f27

Requirements
Must have
• Clear logo and professional direction.
Nice to have
• Use of initials as a possible logo
Should not have
• Graphics/pictures of houses, house roofs etc. Can be an abstracted form of a building.

```html
<!DOCTYPE html>
<html lang="en">
<head>
<meta charset="utf-8">
<title>Varlo Building Pty Ltd – Business Card</title>
<link href="https://fonts.googleapis.com/css2?family=Open+Sans:wght@400;600;700&display=swap" rel="stylesheet">
<style>
  :root {
    --backdrop: #cbcbcd;
    --card-black: #000000;
    --card-white: #ffffff;
    --brand-red: #ec1f27;
    --band-red: #c8090f;
    --ink: #111111;
    --ink-soft: #444444;
    --rule: #8a8a8a;
  }
  html, body {
    margin: 0;
    padding: 0;
    width: 1200px;
    height: 1200px;
    overflow: hidden;
    background: var(--backdrop);
    font-family: "Open Sans", Arial, sans-serif;
  }
  .canvas {
    position: relative;
    width: 1200px;
    height: 1200px;
  }
  .card {
    position: absolute;
    left: 220px;
    width: 760px;
    height: 434px;
    box-shadow: 0 10px 28px rgba(0,0,0,0.25);
    overflow: hidden;
  }
  .card--front {
    top: 110px;
    background: var(--card-black);
    display: flex;
    align-items: center;
    justify-content: center;
  }
  .card--back {
    top: 656px;
    background: var(--card-white);
  }
  .wordmark {
    display: flex;
    align-items: center;
    gap: 16px;
  }
  .wordmark__mark {
    width: 22px;
    height: 22px;
    background: var(--brand-red);
  }
  .wordmark__name {
    font-weight: 600;
    font-size: 44px;
    letter-spacing: 1px;
    text-transform: uppercase;
    line-height: 1;
  }
  .card--front .wordmark__name { color: var(--card-white); }
  .card--back .wordmark {
    position: absolute;
    left: 60px;
    top: 186px;
  }
  .card--back .wordmark__name {
    color: var(--ink);
    font-size: 34px;
  }
  .card--back .wordmark__mark { width: 18px; height: 18px; }
  .divider {
    position: absolute;
    left: 408px;
    top: 92px;
    width: 2px;
    height: 210px;
    background: var(--rule);
  }
  .contact {
    position: absolute;
    left: 440px;
    top: 78px;
    color: var(--ink-soft);
  }
  .contact__name {
    margin: 0;
    font-size: 30px;
    font-weight: 600;
    color: var(--ink);
    line-height: 1.15;
  }
  .contact__role {
    margin: 0 0 22px;
    font-size: 17px;
    color: var(--brand-red);
  }
  .contact__address {
    margin: 0 0 22px;
    font-size: 16px;
    line-height: 1.35;
  }
  .contact__list {
    list-style: none;
    margin: 0;
    padding: 0;
    font-size: 16px;
    line-height: 1.5;
  }
  .contact__list li {
    display: flex;
    align-items: center;
    gap: 10px;
  }
  .contact__list svg { width: 14px; height: 14px; fill: var(--brand-red); }
  .footer-band {
    position: absolute;
    left: 0;
    bottom: 0;
    width: 760px;
    height: 40px;
  }
</style>
</head>
<body>
<div class="canvas">
  <section class="card card--front">
    <div class="wordmark">
      <span class="wordmark__mark"></span>
      <span class="wordmark__name">Varlo Building</span>
    </div>
  </section>

  <section class="card card--back">
    <div class="wordmark">
      <span class="wordmark__mark"></span>
      <span class="wordmark__name">Varlo Building</span>
    </div>
    <div class="divider"></div>
    <div class="contact">
      <p class="contact__name">Daniel Harper</p>
      <p class="contact__role">President</p>
      <p class="contact__address">55 demo street, demo place<br>P.O. Box 000, 555 Avenue</p>
      <ul class="contact__list">
        <li>
          <svg viewBox="0 0 16 16"><path d="M3.6 1.2l2.2 2.6-1.2 1.8c.9 2 2.6 3.8 4.8 4.8l1.8-1.2 2.6 2.2-1.4 2.6C6.8 13.6 2.4 9.2 1 3.2z"/></svg>
          <span>(203) 555-0147</span>
        </li>
        <li>
          <svg viewBox="0 0 16 16"><path d="M1 3h14v1.2L8 9 1 4.2z"/><path d="M1 5.8l7 4.8 7-4.8V13H1z"/></svg>
          <span>info@yourwebsite.com</span>
        </li>
        <li>
          <svg viewBox="0 0 16 16"><circle cx="8" cy="8" r="7"/><path d="M1 8h14M8 1c2.5 2.5 2.5 11.5 0 14M8 1c-2.5 2.5-2.5 11.5 0 14" stroke="#fff" stroke-width="1.2" fill="none"/></svg>
          <span>www.yourwebsite.com</span>
        </li>
      </ul>
    </div>
    <svg class="footer-band" viewBox="0 0 760 40" preserveAspectRatio="none">
      <polygon points="0,20 492,20 484,40 0,40" fill="var(--card-black)"/>
      <polygon points="500,6 760,6 760,40 490,40" fill="var(--band-red)"/>
    </svg>
  </section>
</div>
</body>
</html>
```